Business Card Design

We need a Business card design for our Family Dental Clinic.
Colour choices - White, blue and golden to go with the logo.
Industry/Entity Type
Business
Contact Information for Business Card
Side 1
DR MONA PELLINGHAM
BDS
Suite 6, Level 2, 418 Wexbridge Street
Carlton North, VIC 3054
Fax : 9476 2035
Email: info@fernvaledentalgroup.com.au
Website: fernvaledentalgroup.com.au
Phone(image) - 9476 2035 (bigger size)
Please make sure that you produce 3 files with the same design
1) As per above
2) With out the Name ( i. e DR Mona Pellingham BDS)
3) Just the card template (no texts)
Side 2
......................................... at ........................
Please give 24 hours notice if you cannot keep this appointment

```html
<!DOCTYPE html>
<html lang="en">
<head>
<meta charset="utf-8">
<title>Fernvale Dental Group – Business Card</title>
<link rel="stylesheet" href="https://fonts.googleapis.com/css2?family=Exo+2:wght@400;600;700&display=swap">
<style>
  :root{
    --page:#ecebe8;
    --card:#ffffff;
    --card-shade:#f1f1f1;
    --frame:#f08a1c;
    --blue:#1a4fd6;
    --blue-deep:#0c35b0;
    --ink:#3a3a3a;
    --muted:#6b6b6b;
    --rule:#9a9a9a;
  }
  *{box-sizing:border-box;margin:0;padding:0}
  html,body{width:1069px;height:1200px;overflow:hidden;background:var(--page);font-family:"Exo 2",sans-serif}
  .canvas{position:relative;width:1069px;height:1200px}
  .card{position:absolute;left:154px;width:760px;height:434px;background:linear-gradient(135deg,var(--card) 55%,var(--card-shade));border:14px solid var(--frame);box-shadow:0 10px 30px rgba(0,0,0,.18);overflow:hidden}
  .card--front{top:126px}
  .card--back{top:640px}

  .brand{position:absolute;display:flex;align-items:center;gap:14px}
  .brand__dot{width:44px;height:44px;border-radius:50%;background:var(--blue);flex:none}
  .brand__name{font-weight:600;color:var(--blue-deep);font-size:30px;letter-spacing:2px;text-transform:uppercase;line-height:1;white-space:nowrap}
  .card--front .brand{left:90px;top:90px}
  .card--back .brand{left:50px;top:72px}
  .card--back .brand__name{font-size:22px;letter-spacing:1.5px}
  .card--back .brand__dot{width:34px;height:34px}

  .appointment{position:absolute;left:90px;right:60px;top:190px;color:var(--ink)}
  .appointment__slot{display:flex;align-items:flex-end;gap:12px;font-size:16px;margin-bottom:22px}
  .appointment__line{flex:1;border-bottom:1.5px dotted var(--rule);height:20px}
  .appointment__line--short{flex:0 0 180px}
  .appointment__note{font-size:14px;color:var(--muted);letter-spacing:.3px}

  .web-band{position:absolute;left:0;right:0;bottom:18px;height:44px;background:linear-gradient(90deg,var(--blue-deep),var(--blue));display:flex;align-items:center;justify-content:flex-end;padding-right:40px}
  .web-band__url{color:#fff;font-size:14px;letter-spacing:2px}

  .contacts{position:absolute;right:28px;top:26px;list-style:none}
  .contacts li{display:flex;align-items:center;justify-content:flex-end;gap:12px;height:26px;font-size:13px;color:var(--ink);letter-spacing:.5px;white-space:nowrap}
  .contacts svg{width:16px;height:16px;fill:none;stroke:var(--ink);stroke-width:1.6;flex:none}

  .name-band{position:absolute;left:0;right:0;top:214px;height:80px;background:linear-gradient(90deg,var(--blue-deep),var(--blue) 60%);display:flex;align-items:center;justify-content:space-between}
  .name-band__name{color:#fff;font-weight:700;font-size:36px;letter-spacing:1px;padding-left:40px;white-space:nowrap}
  .name-band__role{height:100%;display:flex;align-items:center;padding:0 48px;background:var(--blue-deep);color:#fff;font-size:16px;font-weight:600;letter-spacing:3px}
  .address{position:absolute;left:40px;top:318px;font-size:14px;line-height:22px;color:var(--muted);letter-spacing:.5px}
</style>
</head>
<body>
<main class="canvas">

  <section class="card card--front" aria-label="Card front with appointment reminder">
    <div class="brand">
      <span class="brand__dot"></span>
      <span class="brand__name">Fernvale Dental Group</span>
    </div>
    <div class="appointment">
      <p class="appointment__slot">
        <span class="appointment__line"></span>
        <span>at</span>
        <span class="appointment__line appointment__line--short"></span>
      </p>
      <p class="appointment__note">Please give 24 hours notice if you cannot keep this appointment</p>
    </div>
    <div class="web-band"><span class="web-band__url">fernvaledentalgroup.com.au</span></div>
  </section>

  <section class="card card--back" aria-label="Card back">
    <div class="brand">
      <span class="brand__dot"></span>
      <span class="brand__name">Fernvale Dental Group</span>
    </div>

    <ul class="contacts">
      <li>9476 2035
        <svg viewBox="0 0 16 16"><path d="M4 1.5l2.5 3-1.5 1.5c.8 2 2.5 3.7 4.5 4.5L11 9l3 2.5-1.5 2.5C7 14 2 9 2 3z"/></svg>
      </li>
      <li>Fax : 9476 2035
        <svg viewBox="0 0 16 16"><rect x="2" y="6" width="12" height="6"/><rect x="4.5" y="2" width="7" height="4"/><rect x="4.5" y="10" width="7" height="4"/></svg>
      </li>
      <li>info@fernvaledentalgroup.com.au
        <svg viewBox="0 0 16 16"><rect x="1.5" y="3.5" width="13" height="9"/><path d="M1.5 3.5L8 9l6.5-5.5"/></svg>
      </li>
      <li>fernvaledentalgroup.com.au
        <svg viewBox="0 0 16 16"><circle cx="8" cy="8" r="6.5"/><path d="M1.5 8h13M8 1.5c-3 3.5-3 9.5 0 13M8 1.5c3 3.5 3 9.5 0 13"/></svg>
      </li>
    </ul>

    <div class="name-band">
      <span class="name-band__name">DR MONA PELLINGHAM</span>
      <span class="name-band__role">BDS</span>
    </div>

    <p class="address">Suite 6, Level 2, 418 Wexbridge Street<br>Carlton North, VIC 3054</p>
  </section>

</main>
</body>
</html>
```